Lumora business card for a plastic surgeon

we need a business card for plastic surgeons that work on a clinic called LUMORA.
we want a clean design and the following informations: name of the doctor, doctor's registration number (called CRM), telephone, address, facebook, instagram.
Colors: white, blue tones, light brown/ coffee

facebook and instagram: lumoracirurgiaestetica

Industry/Entity Type

Business

Contact Information for Business Card

clean design

Font styles to use
Serif
Sans Serif
Other font styles liked:
• helvetica light

Colors
cee9f5
85cae6
85abd2
3276b5
cfeae6
cedeed
eaf1f7

Requirements
Must have
• doctor's name
• identification number (called CRM)
• contact (phone, facebook, instagram, address)

```html
<!DOCTYPE html>
<html lang="pt">
<head>
<meta charset="utf-8">
<title>Lumora – Business Card</title>
<link rel="stylesheet" href="https://fonts.googleapis.com/css2?family=Cinzel:wght@400&family=Lato:wght@400;700&display=swap">
<style>
  :root {
    --page-bg: #dce6f6;
    --card-white: #ffffff;
    --navy: #1a365f;
    --cyan: #26b6d6;
    --frame-white: #ffffff;
  }
  * { margin: 0; padding: 0; box-sizing: border-box; }
  html, body { width: 1200px; height: 965px; overflow: hidden; }
  body { background: var(--page-bg); position: relative; font-family: "Lato", Arial, sans-serif; }

  .card {
    position: absolute;
    left: 285px;
    width: 630px;
    height: 360px;
    border-radius: 18px;
  }
  .card-front { top: 80px; background: var(--card-white); }
  .card-back { top: 526px; background: var(--navy); }

  .card-frame {
    position: absolute;
    left: 37px; top: 39px;
    width: 555px; height: 277px;
    border-radius: 24px;
    border: 3px solid var(--navy);
  }
  .card-back .card-frame { border-color: var(--frame-white); }

  .brand-name {
    position: absolute;
    font-family: "Cinzel", Georgia, serif;
    font-weight: 400;
    letter-spacing: 1px;
    line-height: 1;
  }
  .card-front .brand-name { left: 58px; top: 143px; font-size: 50px; color: var(--cyan); }
  .card-back .brand-name { left: 0; width: 630px; text-align: center; top: 145px; font-size: 54px; color: var(--frame-white); }

  .doctor {
    position: absolute;
    right: 63px; top: 64px;
    text-align: right;
  }
  .doctor-name { font-weight: 700; font-size: 23px; color: var(--navy); line-height: 1.1; }
  .doctor-crm { font-size: 16px; color: var(--cyan); line-height: 1.3; }

  .contact-list {
    position: absolute;
    right: 58px; top: 185px;
    list-style: none;
  }
  .contact-item {
    display: flex;
    justify-content: flex-end;
    align-items: center;
    gap: 14px;
    font-size: 16.5px;
    color: var(--navy);
    height: 21px;
  }
  .contact-icon { width: 15px; height: 15px; flex: none; }

  .address {
    position: absolute;
    right: 59px; top: 264px;
    text-align: right;
    font-size: 16.5px;
    line-height: 21px;
    color: var(--navy);
  }
</style>
</head>
<body>
  <section class="card card-front">
    <div class="card-frame"></div>
    <div class="brand-name">LUMORA</div>

    <div class="doctor">
      <div class="doctor-name">Dr. Marco Reis</div>
      <div class="doctor-crm">CRM #0000</div>
    </div>

    <ul class="contact-list">
      <li class="contact-item">
        <span>(+055).987 654 3210</span>
        <svg class="contact-icon" viewBox="0 0 16 16" aria-hidden="true">
          <circle cx="8" cy="8" r="8" fill="var(--cyan)"/>
          <path d="M5.2 4.2l1.4-.3 1 2.1-.9.8c.5 1.1 1.3 1.9 2.4 2.4l.8-.9 2.1 1-.3 1.4c-3.4.2-6.6-3-6.5-6.5z" fill="#fff"/>
        </svg>
      </li>
      <li class="contact-item">
        <span>/lumoracirurgiaestetica</span>
        <svg class="contact-icon" viewBox="0 0 16 16" aria-hidden="true"><circle cx="8" cy="8" r="8" fill="var(--cyan)"/></svg>
      </li>
      <li class="contact-item">
        <span>/lumoracirurgiaestetica</span>
        <svg class="contact-icon" viewBox="0 0 16 16" aria-hidden="true"><circle cx="8" cy="8" r="8" fill="var(--cyan)"/></svg>
      </li>
    </ul>

    <div class="address">
      Your Address and Suite #<br>
      Zip code, State name here
    </div>
  </section>

  <section class="card card-back">
    <div class="card-frame"></div>
    <div class="brand-name">LUMORA</div>
  </section>
</body>
</html>
```